Label Design For "TUB HALO". All natural liquid water treatment for hot tubs & spas.

Launching a new all natural product to the spa & hot tub market. It's an enzyme based liquid that will come in an aluminum bottle, roughly 500ml.
Allows the user to use far less harsh chemicals in their hot tub while making the water softer and smoother on your skin.

Product is called TUB HALO. The reason for the name is that it uses zero chemicals, zero waste, zero animal testing, and zero effort to use it in your hot tub care routine.

There is no logo, icon, or font. Please feel free to use creative freedom with fonts. Looking for a bold, clean, minimal font for the name, preferably sans serif. A modern bold look that's really clean and minimal is what I'm looking for. The name itself will most likely be the logo. Feel free to spell the word zero or use the number 0 instead in the name.

All of our competition uses a white plastic bottle with a navy blue label. I would like to look completely different from them on a shelf. Something that implies it's natural and soft, and not old, clinical, and industrial.

These are eco friendly products with eco friendly packaging, but I don't want to use green or blue in the colours. Im obviously not a designer at all so please let your ideas flow. I like pastels or bold colours, even black and white. If you have better ideas, I'm open to suggestion. I have attached a couple images that show what my competition looks like and also some design looks and colours I like.

Target Market(s)

Spa & hot tub owners that use their own chemicals weekly/monthly - 80% Male / 20% Female

Industry/Entity Type

Hot Tub Chemicals & Water Care

Font styles to use
Sans Serif

Requirements
Must have
• Clean, Minimal, Modern. Sans Serif Font. The name "TUB HALO". Mention that it's all natural, eco friendly water conditioner for hot tubs and spas.
Nice to have
• Multiple mockups with different colour pallets
Should not have
• Please not busy looking, and please no use of blue or green.

```html
<!DOCTYPE html>
<html lang="en">
<head>
<meta charset="UTF-8">
<title>TUB HALO – Label</title>
<link href="https://fonts.googleapis.com/css2?family=Poppins:wght@300;400;500&display=swap" rel="stylesheet">
<style>
  :root {
    --canvas: #f5f5f5;
    --label: #ebebeb;
    --ink: #1f1f1f;
    --ink-soft: #2b2b2b;
    --rule: #6a6a6a;
    --icon: #a9a9a9;
  }
  html, body {
    margin: 0;
    padding: 0;
    width: 1200px;
    height: 960px;
    overflow: hidden;
    background: var(--canvas);
  }
  .label {
    position: absolute;
    left: 391px;
    top: 50px;
    width: 418px;
    height: 860px;
    background: linear-gradient(180deg, #eeeeee 0%, var(--label) 100%);
    border-radius: 9px;
    font-family: "Poppins", sans-serif;
    color: var(--ink);
  }
  .brand-name {
    position: absolute;
    left: 50px;
    top: 82px;
    margin: 0;
    font-weight: 500;
    font-size: 58px;
    line-height: 1;
    letter-spacing: -0.5px;
    white-space: nowrap;
    color: var(--ink);
  }
  .tagline {
    position: absolute;
    right: 54px;
    top: 364px;
    width: 320px;
    margin: 0;
    text-align: right;
    font-weight: 300;
    font-size: 27px;
    line-height: 33px;
    color: var(--ink-soft);
  }
  .tagline-rule {
    position: absolute;
    left: 53px;
    right: 0;
    top: 478px;
    height: 0;
    border-top: 1.5px solid var(--rule);
  }
  .promises {
    position: absolute;
    left: 62px;
    top: 648px;
    width: 290px;
    display: flex;
    justify-content: space-between;
    list-style: none;
    margin: 0;
    padding: 0;
  }
  .promise {
    width: 84px;
    display: flex;
    flex-direction: column;
    align-items: center;
    color: var(--icon);
  }
  .promise-icon {
    width: 50px;
    height: 56px;
    border-radius: 8px;
    background: #dcdcdc;
  }
  .promise-word {
    margin-top: 4px;
    font-weight: 300;
    font-size: 19px;
    line-height: 1;
  }
  .promise-detail {
    font-weight: 500;
    font-size: 8px;
    line-height: 1.3;
    letter-spacing: 0.2px;
    text-transform: uppercase;
    white-space: nowrap;
  }
  .promise-detail.small { font-size: 5.5px; }
  .volume {
    position: absolute;
    left: 0;
    right: 0;
    top: 794px;
    margin: 0;
    text-align: center;
    font-weight: 400;
    font-size: 24px;
    line-height: 1;
    color: var(--ink-soft);
  }
</style>
</head>
<body>
  <main class="label">
    <h1 class="brand-name">TUB HALO</h1>
    <p class="tagline">All natural liquid water treatment for hot tubs &amp; spas.</p>
    <div class="tagline-rule"></div>
    <ul class="promises">
      <li class="promise">
        <div class="promise-icon" role="img" aria-label="Line icon of a lab flask with bubbles"></div>
        <span class="promise-word">ZERO</span>
        <span class="promise-detail">Chemicals</span>
      </li>
      <li class="promise">
        <div class="promise-icon" role="img" aria-label="Line icon of a recycling bin"></div>
        <span class="promise-word">ZERO</span>
        <span class="promise-detail">Waste</span>
      </li>
      <li class="promise">
        <div class="promise-icon" role="img" aria-label="Line icon of a rabbit and dropper in a crossed circle"></div>
        <span class="promise-word">ZERO</span>
        <span class="promise-detail small">Animal Testing</span>
      </li>
    </ul>
    <p class="volume">500 ml</p>
  </main>
</body>
</html>
```